Pivora has a great new logo - now we need a website!!

Pivora has been in business for a long time and needs to start a new era. Additional to other changes being made in the business itself, Pivora needs an overhaul of its entire branding. PART 1 is COMPLETE - we have our new logo!

Next step... new website! That's where you come in.

Pivora provides a range of computer related services including computer maintenance, networking, sales & cloud services. We provide onsite (field) and remote support. Our customers range from homes to companies with 100+ computers. We pride ourselves on clear and honest communication.

We are a small business but want a professional yet easy-going look that shows the 'cool' side of having your computer system cared for. The website should exude trustworthiness and professionalism but still get comments like 'modern' and 'smart design'. We want our customers to feel that choosing any other company to maintain their system would be a 'geeky' choice.

We like clear thinking so an uncluttered, well organised structure is appreciated. Obvious references to calling or emailing us would be good so people dont need to search around for our contact details.

We look after both Quince & Veltharon operating systems so there needs to be universal appeal rather than a look associated with only one of these two brands.

We want to wow our current clients but also attract new ones so a focus on SEO is a must. And a focus on social media too with links/feeds to Chatterly, chirpex and WorkLoop!

Have a look at www.pivora.com.au so you can see for yourself how much you can help us!

**Breathe new life into Pivora's online presence!**

(We do have a separate website www.kelbrohome.com.au that we set as the homepage for our clients - we like how it is but it might need freshening up to match our new site. We will also want our chatterly page totally made over. You'll probably have other suggestions of things we should be doing. We want to form an ongoing relationship with the right designer!)

(Also, we are open to suggestions regarding the logo size and colour)
Updates

I dont want to cramp anyones creativity but i like this: http://www.quindlework.com/demo/themes/wordpress/2011/saffron/

I'm obivously happy to see your own ideas too!

I also like this one: http://marbleloft.net/item/dralo-responsive-wordpress-theme/7184206

Clarification: We are looking for a working, implemented website, not just design of the theme. Once the general page layout is done we can do the majority of the content input. But we do want a workable shell with images.

We are open to buying existing themes if that helps. Thanks!

Site also needs email contact form, testimonial submission page, blog (feed to home page), chatterly like button

Reason: I haven't found the ideal one yet... We want some other designers to send their ideas.

Reason: We need a little more time to make our decision.

Target Market(s)

Mainly small to medium businesses but also homes

Industry/Entity Type

Small Business

Requirements
Must have
• SEO
Social Media
That little address bar icon
R in a circle at the bottom of the site to show we have trademarked our company name
A finished product website with content and images that we can modify ourselves over time.

```html
<!DOCTYPE html>
<html lang="en">
<head>
<meta charset="utf-8">
<title>Pivora — IT Solutions &amp; Support</title>
<link href="https://fonts.googleapis.com/css2?family=PT+Sans+Narrow:wght@400;700&family=PT+Sans:wght@400;700&family=Lato:wght@400;700&display=swap" rel="stylesheet">
<style>
:root{
  --nav-blue:#4a5f93;
  --nav-blue-dark:#3d4f7e;
  --btn-blue:#5468a0;
  --accent:#4c5f97;
  --ink:#2f2f2f;
  --body:#555;
  --band:#f0f0f0;
  --footer:#2e3133;
  --footer-dark:#25282a;
  --footer-line:#4a4f52;
  --footer-head:#7d95cf;
  --footer-text:#e6e6e6;
  --c-blue:#1ea5e0;
  --c-orange:#f08c00;
  --c-navy:#0d4a7a;
}
*{margin:0;padding:0;box-sizing:border-box}
html,body{width:1167px;height:1200px;overflow:hidden;background:#fff}
body{position:relative;font-family:"PT Sans Narrow",sans-serif;color:var(--body)}
.abs{position:absolute}

.top-bar{left:0;top:0;width:1167px;height:66px;background:linear-gradient(#3f5287,var(--nav-blue) 40%,var(--nav-blue-dark));border-top:5px solid #2f3f6b}
.main-nav{left:167px;top:15px;display:flex;gap:1px}
.main-nav a{width:103px;height:39px;display:flex;align-items:center;justify-content:center;background:linear-gradient(#6277ae,var(--btn-blue));border:1px solid #7b8fc4;color:#fff;text-decoration:none;font:700 14px "PT Sans Narrow",sans-serif;letter-spacing:1px}
.main-nav a.current{color:#2b3552}

.brand{left:167px;top:75px;width:260px;height:90px}
.brand-dot{left:6px;top:14px;width:62px;height:62px;border-radius:50%;background:var(--accent)}
.brand-name{left:86px;top:14px;font:700 36px/1 "PT Sans",sans-serif;color:#333;letter-spacing:1px}
.brand-tag{left:87px;top:52px;font:400 15px/1 "PT Sans",sans-serif;color:#555}

.social-top{top:101px;width:37px;height:37px;border-radius:50%;display:flex;align-items:center;justify-content:center;color:#fff;font:700 8px "PT Sans",sans-serif}

.hero{left:0;top:177px;width:1167px;height:356px;background:linear-gradient(100deg,#6e6c68 0%,#8b8a86 22%,#a9b7c4 45%,#c6d2dc 70%,#9fb0c0 100%)}
.hero-title{left:167px;top:247px;width:347px;height:67px;background:rgba(76,95,151,.85);color:#fff;font:400 48px "PT Sans Narrow",sans-serif;display:flex;align-items:center;padding-left:13px;letter-spacing:.5px}
.hero-line{left:167px;height:21px;background:rgba(76,95,151,.85);color:#fff;font:400 11.5px "PT Sans Narrow",sans-serif;letter-spacing:.9px;padding:0 10px;display:flex;align-items:center}
.hero-more{left:167px;top:439px;width:75px;height:35px;background:linear-gradient(#3a3a3a,#151515);border:1px solid #555;color:#fff;font:700 14px "PT Sans Narrow",sans-serif;letter-spacing:1px;display:flex;align-items:center;justify-content:center}

.tagline{left:0;top:533px;width:1167px;height:66px;background:var(--band);display:flex;align-items:center;justify-content:center;font:700 28px "PT Sans Narrow",sans-serif;color:var(--ink);letter-spacing:1.6px}
.tagline span{color:var(--accent);margin-left:9px}

.feature{top:636px;width:270px}
.feature-icon{position:absolute;left:0;top:0;width:33px;height:33px;border-radius:50%}
.feature h3{position:absolute;left:45px;top:5px;font:700 17px "PT Sans Narrow",sans-serif;color:var(--ink);letter-spacing:.8px}
.feature p,.about p{font:400 13px/18.3px "PT Sans Narrow",sans-serif;letter-spacing:.35px;color:var(--body)}
.feature p{position:absolute;top:43px;left:0;width:268px}

.about{left:173px;top:806px;width:212px}
.about h2{font:700 17px "PT Sans Narrow",sans-serif;color:var(--ink);letter-spacing:.8px;margin-bottom:6px}
.about-photo{top:796px;width:192px;height:129px;border:3px solid #e4e6ea}

.footer{left:0;top:965px;width:1167px;height:235px;background:linear-gradient(var(--footer),var(--footer-dark));border-top:7px solid var(--accent)}
.footer-head{font:400 10px "Lato",sans-serif;color:var(--footer-head);letter-spacing:1px;padding-bottom:4px;border-bottom:1px solid var(--footer-line);width:223px}
.sitemap{display:grid;grid-template-columns:129px 100px}
.sitemap a{font:400 9.5px/20px "Lato",sans-serif;color:var(--footer-text);text-decoration:none;padding-left:15px;position:relative}
.sitemap a::before{content:"›";position:absolute;left:2px;top:-2px;color:#6f8ad4;font-size:12px}
.follow-icon{width:32px;height:32px;border-radius:50%;background:radial-gradient(circle at 40% 35%,#f2f2f2,#b9b9b9);display:flex;align-items:center;justify-content:center;color:#4a4a4a;font:700 6.5px "Lato",sans-serif;letter-spacing:-.1px}
.copyright{left:460px;top:1134px;width:250px;text-align:center;font:400 9px "Lato",sans-serif;color:var(--footer-text);letter-spacing:.7px}
.copyright b{font-weight:400;color:var(--footer-head)}
.form-label{left:761px;font:400 9.5px "Lato",sans-serif;color:var(--footer-text)}
.form-field{left:804px;width:174px;background:#232628;border:1px solid #4a4f52}
.form-go{left:805px;top:1137px;width:50px;height:22px;background:linear-gradient(#6e86c4,#42579a);border:1px solid #8aa0d6;color:#fff;font:400 10px "Lato",sans-serif;letter-spacing:1px;display:flex;align-items:center;justify-content:center}
</style>
</head>
<body>

<div class="abs top-bar"></div>
<nav class="abs main-nav">
  <a class="current" href="#">HOME</a><a href="#">SERVICES</a><a href="#">PRICING</a><a href="#">HOURS</a><a href="#">PAYMENTS</a><a href="#">LINKS</a><a href="#">NEWS</a><a href="#">CONTACT</a>
</nav>

<div class="abs brand">
  <div class="abs brand-dot"></div>
  <div class="abs brand-name">PIVORA</div>
  <div class="abs brand-tag">IT Solutions &amp; Support</div>
</div>

<div class="abs social-top" style="left:811px;background:var(--c-navy)">Chatterly</div>
<div class="abs social-top" style="left:862px;background:var(--c-blue)">Chirpex</div>
<div class="abs social-top" style="left:912px;background:var(--c-orange)" aria-label="News feed">
  <svg width="37" height="37" viewBox="0 0 37 37"><circle cx="14" cy="23" r="2" fill="#fff"/><path d="M12 16a9 9 0 0 1 9 9M12 11a14 14 0 0 1 14 14" fill="none" stroke="#fff" stroke-width="2.2"/></svg>
</div>
<div class="abs social-top" style="left:963px;background:#c9c9c9" aria-label="Email">
  <svg width="37" height="37" viewBox="0 0 37 37"><rect x="11" y="13" width="15" height="11" fill="none" stroke="#fff" stroke-width="1.5"/><path d="M11 13l7.5 6 7.5-6" fill="none" stroke="#fff" stroke-width="1.5"/></svg>
</div>

<div class="abs hero" role="img" aria-label="Photo of a businessman using a tablet in front of a server room with monitors"></div>
<div class="abs hero-title">HEADLINE HERE</div>
<div class="abs hero-line" style="top:338px">Lorem ipsum dolor sit amet, consectetur adipiscing elit. Nunc vitae fermentu</div>
<div class="abs hero-line" style="top:362px">lorem. In hac habitasse platea dictumst. Morbi tincidunt massa vitae loremon</div>
<div class="abs hero-line" style="top:386px">euismod laore ellert onmous olloner</div>
<div class="abs hero-more">MORE</div>

<div class="abs tagline">Duis sagittis metus in quam <span>ornare ultrices oplening elli</span></div>

<div class="abs feature" style="left:173px">
  <div class="feature-icon" style="background:var(--c-blue)">
    <svg width="33" height="33" viewBox="0 0 33 33" fill="#fff"><circle cx="16.5" cy="13" r="3.2"/><path d="M10.5 23c0-4 2.7-6 6-6s6 2 6 6z"/><circle cx="10.5" cy="14.5" r="2.3"/><path d="M6 22.5c0-3 1.8-4.5 4.5-4.5 1 0 1.6.2 2 .5-1.2 1-1.8 2.4-2 4z"/><circle cx="22.5" cy="14.5" r="2.3"/><path d="M27 22.5c0-3-1.8-4.5-4.5-4.5-1 0-1.6.2-2 .5 1.2 1 1.8 2.4 2 4z"/></svg>
  </div>
  <h3>Collaborate</h3>
  <p>Fusce egestas luctus lacus vitae hendrerit. Morbi vitae nibh erat, non aliquet diam. Curabitur odio mauris, suscipit non blandit iaculis, tempor quis velit. Sed consequat justo et massa.</p>
</div>
<div class="abs feature" style="left:456px">
  <div class="feature-icon" style="background:var(--c-orange)">
    <svg width="33" height="33" viewBox="0 0 33 33"><rect x="9" y="9" width="15" height="15" fill="none" stroke="#fff" stroke-width="1.3"/><path d="M11.5 21l4-4 2.5 2 4-5.5" fill="none" stroke="#fff" stroke-width="1.6"/></svg>
  </div>
  <h3>Grow</h3>
  <p>Fusce egestas luctus lacus vitae hendrerit. Morbi vitae nibh erat, non aliquet diam. Curabitur odio mauris, suscipit non blandit iaculis, tempor quis velit. Sed consequat justo et massa.</p>
</div>
<div class="abs feature" style="left:730px">
  <div class="feature-icon" style="background:var(--c-navy)">
    <svg width="33" height="33" viewBox="0 0 33 33" fill="none" stroke="#fff" stroke-width="1.4"><ellipse cx="14" cy="11" rx="5.5" ry="2"/><path d="M8.5 11v9c0 1.1 2.5 2 5.5 2M8.5 14c0 1.1 2.5 2 5.5 2s5.5-.9 5.5-2M8.5 17c0 1.1 2.5 2 5.5 2M19.5 11v3"/><circle cx="20" cy="20" r="4.5" fill="#5aa7d6" stroke="#fff"/></svg>
  </div>
  <h3>Cost Effective</h3>
  <p>Fusce egestas luctus lacus vitae hendrerit. Morbi vitae nibh erat, non aliquet diam. Curabitur odio mauris, suscipit non blandit iaculis, tempor quis velit. Sed consequat justo et massa.</p>
</div>

<div class="abs about">
  <h2>About our Company</h2>
  <p>Fusce egestas luctus lacus vitae hendrerit. Morbi vitae nibh erat, non aliquet diam. Curabitur odio mauris, suscipit non blandit iaculis, tempor quis velit. Sed consequat</p>
</div>
<div class="abs about-photo" style="left:406px;background:linear-gradient(135deg,#5d8fc0,#b9d4ea 60%,#7aa3c9)" role="img" aria-label="Photo of hands typing on a laptop keyboard"></div>
<div class="abs about-photo" style="left:608px;background:linear-gradient(120deg,#7d7e80,#d8c4a8 55%,#efe6dc)" role="img" aria-label="Photo of two colleagues working at a computer"></div>
<div class="abs about-photo" style="left:809px;background:linear-gradient(180deg,#e6ebec,#d6dcdc 60%,#c8a878)" role="img" aria-label="Photo of a bright office with a desk and chair"></div>

<div class="abs footer"></div>

<div class="abs" style="left:194px;top:1008px">
  <div class="footer-head">SITEMAP</div>
  <div class="sitemap" style="margin-top:5px">
    <a href="#">Our Service</a><a href="#">About Us</a>
    <a href="#">Who we are</a><a href="#">Chatterly</a>
    <a href="#">Training</a><a href="#">Chirpex</a>
    <a href="#">Pay a bill</a><a href="#">News</a>
    <a href="#">Certifications</a><a href="#">Our Story</a>
    <a href="#">Pricing</a><a href="#">Contact</a>
  </div>
</div>

<div class="abs" style="left:474px;top:1008px"><div class="footer-head">FOLLOW US</div></div>
<div class="abs follow-icon" style="left:494px;top:1043px">Chirpex</div>
<div class="abs follow-icon" style="left:567px;top:1043px">Chatterly</div>
<div class="abs follow-icon" style="left:638px;top:1043px" aria-label="Calendar">
  <svg width="32" height="32" viewBox="0 0 32 32"><rect x="10" y="10" width="12" height="12" rx="1.5" fill="#5a5a5a"/><path d="M16 13v6M13 16h6" stroke="#ddd" stroke-width="1.6"/></svg>
</div>
<div class="abs follow-icon" style="left:494px;top:1086px">Dotrally</div>
<div class="abs follow-icon" style="left:567px;top:1086px">Vidlo</div>
<div class="abs follow-icon" style="left:638px;top:1086px" aria-label="News feed">
  <svg width="32" height="32" viewBox="0 0 32 32"><circle cx="12.5" cy="20" r="1.8" fill="#555"/><path d="M10.5 14a7.5 7.5 0 0 1 7.5 7.5M10.5 10a11.5 11.5 0 0 1 11.5 11.5" fill="none" stroke="#555" stroke-width="2"/></svg>
</div>
<div class="abs copyright">© Copyright <b>Pivora</b> 2012 &nbsp;<b>|</b>&nbsp; All rights reserved</div>

<div class="abs" style="left:760px;top:1008px"><div class="footer-head" style="width:219px">CONTACT US</div></div>
<div class="abs form-label" style="top:1039px">Name</div>
<div class="abs form-field" style="top:1034px;height:21px"></div>
<div class="abs form-label" style="top:1064px">Email</div>
<div class="abs form-field" style="top:1060px;height:21px"></div>
<div class="abs form-label" style="top:1089px">Message</div>
<div class="abs form-field" style="top:1086px;height:44px"></div>
<div class="abs form-go">GO</div>

</body>
</html>
```